Harbor - Security & Risk Management Firm needs a flier designed

Our firm needs a one page, front and back flier designed to represent our services. The one side of the flier should highlight our premium guard services, as we only hire prior military and law enforcement personnel. The reverse, should promote our Remote Video Guarding Service. OUr firm is owned and operated by U.S. Military and law enforcement veterans.

Target Market(s)

Commercial and Government Clients

Industry/Entity Type

Security Service

Font styles to use
Sans Serif

Colors

Designer to choose colors to be used in the design.

Requirements
Must have
• SIDE 1: Highlight Professional Guard Services, with highlighted points
• - No Long Term Contracts! Month-to-month terms
• - All armed officers have minimum 5+ years U.S. Military and/or law enforcement experience
• - Officers are trained in Active Shooter Response
• - Professional, Courteous and Dependable
• SIDE 2: Highlight Remote Video Guarding Services
• "OUR KORVEX, REMOTE VIDEO GUARDING SOLUTION, IS TRUSTED BY THOUSANDS OF SATISFIED CUSTOMERS. ANY SUSPICIOUS OR CRIMINAL ACTIVITY IS MET WITH OUR TRAINED AND LICENSED OPERATORS WHO IDENTIFY THE SITUATION, SOUND SIRENS, TURN ON LIGHTS, CONTACT CUSTOMERS AND DISPATCH LAW ENFORCEMENT OR LOCAL SECURITY TEAMS. WE LEAD THE INDUSTRY IN UNMATCHED PROFESSIONALISM, EXPERTISE, INDUSTRY LEADING RESOLUTION, ANALYTICS, AND INTRUSION DETECTION.
• EXPERIENCE THE BALDOMAR DIFFERENCE TODAY, BY CONTACTING OUR TEAM NOW FOR A FREE CONSULTATION."
• Starting as low as $795/month
• DESIGN STYLE: The design should reflect a high end, professional brand. But should also have some of a tactical feel, that represents our foundation of military and law enforcement professionals.
• Colors: Company colors are Navy Blue and Silver/Grey - These are the colors that should be used, to match our logo
• Contact info:
• Web: www.BALDOMAR-example.com
• Phone: 1-833-555-0142
• Must include our logo, company name, and contact info on bottom of each side.
• Flier size 8.5"x11"
• Final project should be delivered in Photoshop or Adobe Illustrator
Nice to have
• I like the use of images inside or mixed with shapes such as hexagons.
• Feel free to use our website: www.baldomar-example.com and use any content or imagery in the design.
• I also like conveying messages with images and icons. Want the overall feel to be clean and simple.
• We are trying to create our brand and the flier should be a good representation of our brand.

```html
<!DOCTYPE html>
<html lang="en">
<head>
<meta charset="utf-8">
<title>Professional Guard Services – Baldomar</title>
<link rel="stylesheet" href="https://fonts.googleapis.com/css2?family=Archivo:wdth,wght@62..125,900&family=Exo+2:ital,wght@1,800&family=Montserrat:wght@400;700;800&display=swap">
<style>
  :root {
    --navy-deep: #0d2350;
    --navy: #123a7a;
    --blue: #1d6fc0;
    --cyan: #2fa6e0;
    --lime: #cde13c;
    --lime-soft: #d8e64a;
    --white: #ffffff;
    --ink: #1d2a44;
  }
  * { margin: 0; padding: 0; box-sizing: border-box; }
  html, body { width: 934px; height: 1200px; overflow: hidden; background: var(--navy-deep); }
  .flier {
    position: relative; width: 934px; height: 1200px; overflow: hidden;
    background:
      radial-gradient(ellipse 520px 360px at 40px 20px, rgba(205,225,60,.85), rgba(205,225,60,0) 70%),
      radial-gradient(ellipse 600px 700px at 300px 560px, var(--cyan), rgba(47,166,224,0) 75%),
      linear-gradient(180deg, #1b7fc6 0%, #1661ad 45%, var(--navy) 75%, var(--navy-deep) 100%);
    font-family: "Montserrat", sans-serif;
  }
  .decor { position: absolute; inset: 0; }
  .hero-figure {
    position: absolute; left: 430px; top: 0; width: 504px; height: 1080px;
    background: radial-gradient(ellipse 260px 520px at 300px 480px, rgba(10,30,70,.75), rgba(10,30,70,.35) 60%, rgba(10,30,70,0) 100%);
  }
  .headline { position: absolute; left: 0; top: 0; width: 934px; height: 760px; color: var(--white); font-family: "Archivo", sans-serif; font-weight: 900; line-height: 1; }
  .headline span { position: absolute; white-space: nowrap; }
  .headline .line-top { left: 90px; top: 453px; font-size: 64px; font-stretch: 78%; }
  .headline .line-main {
    left: -4px; top: 485px; font-size: 222px; font-stretch: 92%; letter-spacing: -5px;
    background: linear-gradient(180deg, #fff 45%, #bfe6fb 100%); -webkit-background-clip: text; background-clip: text; color: transparent;
  }
  .headline .line-bottom { left: 246px; top: 682px; font-size: 62px; font-stretch: 82%; }
  .offer { position: absolute; left: 0; top: 858px; width: 620px; font-family: "Exo 2", sans-serif; font-style: italic; font-weight: 800; color: var(--lime); font-size: 33px; line-height: 37px; }
  .offer span { display: block; white-space: nowrap; }
  .offer .o1 { padding-left: 108px; }
  .offer .o2 { padding-left: 122px; }
  .points { position: absolute; left: 47px; top: 957px; width: 520px; text-align: center; color: var(--white); font-size: 17.5px; line-height: 22px; letter-spacing: .3px; }
  .points li { list-style: none; margin-bottom: 17px; white-space: nowrap; }
  .brand-panel { position: absolute; left: 598px; top: 960px; width: 288px; height: 240px; }
  .brand-panel svg { position: absolute; inset: 0; }
  .brand { position: absolute; left: 0; right: 0; top: 94px; text-align: center; color: var(--ink); }
  .brand .name { display: inline-flex; align-items: center; gap: 7px; font-weight: 800; font-size: 25px; letter-spacing: .5px; }
  .brand .name i { width: 20px; height: 20px; background: var(--ink); display: inline-block; }
  .brand .tag { font-size: 8.5px; font-weight: 700; letter-spacing: .6px; margin-top: 2px; }
  .contact { position: absolute; left: 0; right: 0; top: 152px; text-align: center; color: var(--ink); font-size: 14px; line-height: 21px; }
  .contact .phone { font-weight: 700; }
</style>
</head>
<body>
<main class="flier">
  <svg class="decor" width="934" height="1200" viewBox="0 0 934 1200">
    <g fill="none" stroke="rgba(205,225,60,.55)" stroke-width="1.5">
      <polygon points="488,180 590,238 590,354 488,412 386,354 386,238"/>
      <polygon points="560,740 686,812 686,955 560,1027 434,955 434,812"/>
      <polygon points="644,164 658,172 658,188 644,196 630,188 630,172"/>
      <polygon points="120,300 230,362 230,488 120,550 10,488 10,362"/>
    </g>
    <g>
      <polygon points="488,180 590,238 590,354 488,412 386,354 386,238" fill="rgba(205,225,60,.25)"/>
      <polygon points="545,176 655,238 655,362 545,424 435,362 435,238" fill="rgba(47,166,224,.35)"/>
      <polygon points="60,700 150,752 150,856 60,908 -30,856 -30,752" fill="rgba(205,225,60,.25)"/>
      <polygon points="450,824 470,836 470,860 450,872 430,860 430,836" fill="rgba(205,225,60,.7)"/>
    </g>
  </svg>

  <div class="hero-figure" role="img" aria-label="Tactical officer in helmet holding a rifle, blended into blue smoke"></div>

  <svg class="decor" width="934" height="1200" viewBox="0 0 934 1200" role="img" aria-label="Uniformed officer saluting, framed in a hexagon">
    <defs>
      <linearGradient id="saluteFill" x1="0" y1="0" x2="1" y2="1">
        <stop offset="0" stop-color="#7fb6d8"/>
        <stop offset="1" stop-color="#244f80"/>
      </linearGradient>
    </defs>
    <polygon points="194,68 356,158 356,338 194,428 32,338 32,158" fill="url(#saluteFill)"/>
  </svg>

  <h1 class="headline">
    <span class="line-top">PROFESSIONAL</span>
    <span class="line-main">GUARD</span>
    <span class="line-bottom">SERVICES</span>
  </h1>

  <p class="offer"><span class="o1">No Long Term Contracts!</span><span class="o2">Month-to-month terms</span></p>

  <ul class="points">
    <li>All armed officers have minimum 5+ years<br>U.S. Military and/or law enforcement experience</li>
    <li>Officers are trained in Active Shooter Response</li>
    <li>Professional, Courteous and Dependable</li>
  </ul>

  <div class="brand-panel">
    <svg width="288" height="240" viewBox="0 0 288 240">
      <polygon points="144,0 288,84 288,240 0,240 0,84" fill="var(--lime-soft)"/>
    </svg>
    <div class="brand">
      <div class="name"><i></i>BALDOMAR</div>
      <div class="tag">—SECURITY &amp; RISK MANAGEMENT—</div>
    </div>
    <div class="contact">
      <div>www.BALDOMAR-example.com</div>
      <div class="phone">1-833-555-0142</div>
    </div>
  </div>
</main>
</body>
</html>
```